Full color cover for Chamber's Membership Menu

I need a cover, 8 1/2" x 11" for our Chamber of Commerce Membership Menu. Is should have our logo and the words, Membership Menu on it. That's all that is necessary but it can include one or more of the other photos (maybe a college?) that I added, though they are not required. Our logo colors should be used: 37-170-226, 58-181-74, 40-56-144, 247-148-29, 189-190-192.

Target Market(s)

Business owners and managers

Industry/Entity Type

Business Development

Font styles to use
Serif

Colors
0054AA
0677BA
7BADD7
CADEEF
E8F1F8
00AB8E
00BBA5
67D7C9
C6EFE9
E9F9F6
F0912C
F2A743
F7CA91
FBE8D2
FDF5EE

Requirements
Must have
• Our logo and the words Membership Menu
Nice to have
• An attractive business-like feel. It can be very simple.

```html
<!DOCTYPE html>
<html lang="en">
<head>
<meta charset="utf-8">
<title>Riverton Chamber – Membership Menu Cover</title>
<link href="https://fonts.googleapis.com/css2?family=Oswald:wght@500;700&display=swap" rel="stylesheet">
<style>
  :root {
    --backdrop: #262626;
    --paper: #ffffff;
    --navy: #283890;
    --navy-deep: #1c2a7a;
    --sky: #25aae2;
    --green: #3ab54a;
    --orange: #f7941d;
    --orange-deep: #f07a1a;
    --silver: #bdbec0;
  }
  html, body {
    margin: 0;
    padding: 0;
    width: 1200px;
    height: 1200px;
    overflow: hidden;
    background: var(--backdrop);
  }
  .cover {
    position: absolute;
    left: 240px;
    top: 126px;
    width: 744px;
    height: 962px;
    display: block;
  }
  .brand-name, .brand-tagline {
    font-family: "Oswald", "Arial Narrow", sans-serif;
    font-weight: 500;
    fill: var(--navy);
  }
  .title {
    font-family: "Oswald", "Arial Narrow", sans-serif;
    font-weight: 700;
  }
  .title-main { fill: #e9eaee; }
  .title-accent { fill: var(--orange); }
</style>
</head>
<body>
<svg class="cover" viewBox="0 0 620 802" xmlns="http://www.w3.org/2000/svg">
  <defs>
    <linearGradient id="skyBand" x1="0" y1="0" x2="1" y2="0">
      <stop offset="0" stop-color="#1f7fc4"/>
      <stop offset="0.6" stop-color="var(--sky)"/>
      <stop offset="1" stop-color="#7fd0f2"/>
    </linearGradient>
    <linearGradient id="orangeBand" x1="0" y1="0" x2="1" y2="0">
      <stop offset="0" stop-color="#f9a53a"/>
      <stop offset="1" stop-color="var(--orange-deep)"/>
    </linearGradient>
    <radialGradient id="navyField" cx="0.4" cy="0.7" r="0.8">
      <stop offset="0" stop-color="#3446a8"/>
      <stop offset="1" stop-color="var(--navy-deep)"/>
    </radialGradient>
    <linearGradient id="photoLeft" x1="0" y1="0" x2="0" y2="1">
      <stop offset="0" stop-color="#8a6a4c"/>
      <stop offset="1" stop-color="#2a2428"/>
    </linearGradient>
    <linearGradient id="photoMiddle" x1="0" y1="0" x2="0" y2="1">
      <stop offset="0" stop-color="#6b4a30"/>
      <stop offset="1" stop-color="#1e1a1c"/>
    </linearGradient>
    <linearGradient id="photoRight" x1="0" y1="0" x2="0" y2="1">
      <stop offset="0" stop-color="#b59a78"/>
      <stop offset="1" stop-color="#3a2a2c"/>
    </linearGradient>
  </defs>

  <!-- page -->
  <rect class="page" x="0" y="0" width="620" height="802" fill="var(--paper)"/>
  <rect class="top-bar" x="0" y="0" width="620" height="8" fill="var(--orange)"/>

  <!-- brand -->
  <g class="brand">
    <circle class="brand-mark" cx="310" cy="85" r="24" fill="var(--navy)"/>
    <text class="brand-name" x="310" y="166" text-anchor="middle" font-size="25" textLength="258" lengthAdjust="spacingAndGlyphs">RIVERTON CHAMBER</text>
    <text class="brand-tagline" x="310" y="183" text-anchor="middle" font-size="12" textLength="258" lengthAdjust="spacing">OF COMMERCE &amp; TOURISM</text>
  </g>

  <!-- photo strip -->
  <g class="photo" role="img" aria-label="Photo of three chamber members smiling at an evening networking event">
    <polygon points="0,300 176,268 166,520 0,520" fill="url(#photoLeft)"/>
  </g>
  <g class="photo" role="img" aria-label="Photo of six culinary students in black aprons standing together in a kitchen">
    <polygon points="176,252 444,248 426,520 166,520" fill="url(#photoMiddle)"/>
  </g>
  <g class="photo" role="img" aria-label="Photo of three women attending a chamber reception">
    <polygon points="450,262 620,262 620,560 428,560" fill="url(#photoRight)"/>
  </g>

  <!-- sky swoosh over photos -->
  <path class="sky-swoosh" d="M0,300 Q140,240 395,238 Q150,258 0,318 Z" fill="url(#skyBand)"/>
  <path class="sky-swoosh-tail" d="M0,286 Q150,232 410,236 Q150,244 0,300 Z" fill="var(--paper)"/>

  <!-- orange arc and navy field -->
  <path class="arc-edge" d="M0,484 Q310,352 620,522 L620,802 L0,802 Z" fill="var(--paper)"/>
  <path class="orange-arc" d="M0,492 Q310,362 620,530 L620,802 L0,802 Z" fill="url(#orangeBand)"/>
  <path class="navy-field" d="M0,508 Q300,394 620,554 L620,802 L0,802 Z" fill="url(#navyField)"/>

  <!-- silver swoosh bottom right -->
  <path class="silver-swoosh" d="M228,792 Q400,672 620,628 L620,662 Q420,700 272,792 Z" fill="var(--silver)"/>
  <path class="white-corner" d="M272,792 Q420,700 620,662 L620,792 Z" fill="var(--paper)"/>

  <!-- title -->
  <text class="title title-main" x="28" y="635" font-size="74" textLength="332" lengthAdjust="spacingAndGlyphs">MEMBERSHIP</text>
  <text class="title title-accent" x="28" y="703" font-size="74" textLength="138" lengthAdjust="spacingAndGlyphs">MENU</text>

  <rect class="bottom-bar" x="0" y="792" width="620" height="10" fill="var(--green)"/>
</svg>
</body>
</html>
```